Poem Handwritten by Veteran while in the jungle of Vietnam

My parents are celebrating their 50th wedding anniversary this year. I wanted to give them a very memorable gift. On my parents 2nd anniversary, my father was stationed in Vietnam. On that night he was in the jungle waiting till morning and wrote a poem to my mother using his pant leg as paper. I would like this poem to typographically designed to be framed and hung on the wall.

I have attached a picture of the poem below. It will need to be 11x14 when printed for framing. It would be great if there was background or artwork to make it more visually interesting, perhaps in a watercolor. My parents have a transitional style. I have attached some possible color schemes as well. Cool greens, blue, neutral grays, with hints of berries or highlights of yellow. These are just a guide, I would be open to your interpretations.

Thank you for your help. This will hopefully be a gift they will truly treasure as much as the poem itself.

Target Market(s)

My parents who are excited to be celebrating their 50th wedding anniversary. It should have a transitional, mature style.

Font styles to use
Serif
Script

Requirements
Must have
• The poem, typographically designed. There can be a mix of fonts, but legibility is critically important.
• Now that some designs have come through I wanted to give some more guidance of what I'm looking for. I want something that feels sophisticated and artistic.
Nice to have
• A background or art work, using the color schemes attached as a guide. I am really liking the designs that have a full color landscape artwork in the background. The fonts should be elegant and formal. I really like the romantic, muted colors. I had trouble finding similar projects online in the style I wanted until I cam across wedding invites. Those seem to be the most applicable. I've added pictures of some so you can get a sense of what I'm looking for. I am really liking the jungle foliage, starry skies or sunrises.
Should not have
• Cartoon caricatures, fonts that are too illegible when printed. I'm not liking anything whimsical. I don't like the very bright colors for this project.

```html
<!DOCTYPE html>
<html lang="en">
<head>
<meta charset="utf-8">
<title>Life's Journey — Anniversary Poem</title>
<link rel="stylesheet" href="https://fonts.googleapis.com/css2?family=Didact+Gothic&family=Pinyon+Script&display=swap">
<style>
  :root {
    --page: #ffffff;
    --mat: #687d8e;
    --banner: #272e43;
    --ink: #ffffff;
    --gold: #e6b93a;
    --leaf-slate: #6b8194;
    --leaf-olive: #5f6631;
    --leaf-yellow: #f7c136;
  }
  html, body {
    margin: 0;
    padding: 0;
    width: 1200px;
    height: 1200px;
    overflow: hidden;
    background: var(--page);
  }
  .canvas {
    position: relative;
    width: 1200px;
    height: 1200px;
  }
  .mat {
    position: absolute;
    left: 157px;
    top: 29px;
    width: 890px;
    height: 1132px;
    background: var(--mat);
  }
  .banner-art {
    position: absolute;
    left: 0;
    top: 0;
    width: 1200px;
    height: 1200px;
  }
  .poem-column {
    position: absolute;
    top: 151px;
    width: 340px;
    margin: 0;
    font-family: "Didact Gothic", "Century Gothic", sans-serif;
    font-size: 15px;
    letter-spacing: 0.35px;
    line-height: 17.1px;
    color: var(--ink);
    text-align: center;
  }
  .poem-column--left { left: 281px; }
  .poem-column--right { left: 590px; }
  .stanza { margin: 0 0 17.1px; }
  .stanza--wide-gap { margin-top: 28px; }
  .drop-cap {
    font-family: "Pinyon Script", cursive;
    font-size: 48px;
    line-height: 0;
    letter-spacing: 0;
    color: var(--gold);
    position: relative;
    top: 6px;
    margin-right: -6px;
  }
</style>
</head>
<body>
<main class="canvas">
  <div class="mat"></div>

  <svg class="banner-art" viewBox="0 0 1200 1200">
    <defs>
      <linearGradient id="foliage-tone" x1="1" y1="0" x2="0" y2="1">
        <stop offset="0" stop-color="#6b8194"/>
        <stop offset="0.4" stop-color="#5f6631"/>
        <stop offset="0.6" stop-color="#b69a34"/>
        <stop offset="1" stop-color="#4a5a6d"/>
      </linearGradient>
    </defs>
    <polygon class="banner" points="272,84 933,84 933,944 602,1094 272,892" fill="var(--banner)"/>
    <path class="foliage" role="img"
          aria-label="Illustration of jungle foliage: slate fronds, olive and yellow leaves, flowers, butterflies and a dragonfly"
          d="M933,440 C840,470 720,560 665,700 C640,780 630,830 610,860 L272,860 L272,892 L602,1094 L933,944 Z"
          fill="url(#foliage-tone)" opacity="0.75"/>
  </svg>

  <section class="poem-column poem-column--left">
    <p class="stanza"><span class="drop-cap">L</span>ife's journey began with a challenge<br>It was heralded far and near<br>The road led on foerever<br>it's completion was known to be clear</p>
    <p class="stanza">From the garden of light proceeded,<br>To the valley of shadows it led<br>Thorns and thistles adorned it<br>Past abyss and crevice it sped</p>
    <p class="stanza stanza--wide-gap">The brave surged forward with courage<br>The wise undaunted pressed on<br>The mighty held their banner<br>We all awaited the dawn</p>
    <p class="stanza">Though the pitfalls and hazards were many<br>The pathways was&nbsp; clearly in view<br>Straight and sure it glided<br>It's course we knew to be true</p>
    <p class="stanza">I knew you, Sweetheart beforehand<br>So precious and sweet were you<br>Our moments of bliss were priceless<br>Each day thought us joy anew</p>
    <p class="stanza">The call to progression beckoned,<br>At last I would have my chance-<br>to clasp you to me forever,<br>And seal our divine romance</p>
    <p class="stanza">I eagerly started the journey<br>Though with sorrow, I left you behind<br>With courage and faith I continued<br>Far I knew that you later I'd find</p>
    <p class="stanza">I dligintly searched for you, Darling<br>The roadway was both bleek and fair<br>Though the years grew long in number<br>I did not give up in despair</p>
  </section>

  <section class="poem-column poem-column--right">
    <p class="stanza">At last in distance I saw you,<br>So beautiful, lovely and sweet!<br>Your attention I struggled to capture,<br>Your love I wrested to meet</p>
    <p class="stanza">What rapture was mine in fulfillment<br>As now together we stand<br>To cherish and love each other,<br>While our plans and dreams expand</p>
    <p class="stanza">I love you, Darling, forever,<br>My life you have made replete,<br>Our eternal mansion beckons,<br>Your love has made it complete</p>
  </section>
</main>
</body>
</html>
```